Motel Sign - Front

(21/03/12 - I've edited the brief and removing the words "garden view" its not fitting in the designs I'm getting and just want the word motel to be the focus. I have a template/vision of what I want - see the whiteboard sketch of what I'm looking for uploaded today. Definitely open to creatively, new designs and different ideas but the whiteboard design I've done should be a guideline. Keep it fresh/green/white. use the sample photos of green as inspiration. Thanks)
We are a motel set in the mountain country of Victoria - Australia. The front of the motel needs a fresh look. We recently removed a large amount of the garden to expose a brick courtyard fence which the front of the courtyard faces out to the main road. Within the courtyard fence there is a wooden frame and paneling.
We want to have a new sign created to slot into the wooden frame. (see photo) its the white component.
Its a very large and unusual shape and I want to keep it simple but need to fill the in the best way possible.
The space is 940mm high and 4940mm width.
The message of the sign is simple the word "MOTEL". I want people to be able to drive past and glance in and see we are a motel straight away. So the main purpose of the sign is to say "MOTEL".
I am open to colour use to match the space and have impact. I thought a background colour should be 'off white'. I'm open to the colours used to match your design as long as it matches the brief. Maybe a garden green for the emblem.
IN BRIEF:
1) the word "MOTEL"
2) Border/Background that ties in the garden.
The design should be centred, clean and simple, doesn't have to fill the whole space as long as its balanced and centred.
I like cursive and garden like designs for this one - as long its the word MOTEL still has impact. (OPEN TO NEW IDEAS)
I am also open to different ideas and suggestions if you feel you have a better way to take advantage of this space.
The sign will be 7-8 metres from the road itself.
NOTE: the photos show the space and the painted white in the space where the sign will go. The garden in front of this space will be completely cleared.
Motel

```html
<!DOCTYPE html>
<html lang="en">
<head>
<meta charset="UTF-8">
<title>Motel Sign – Front</title>
<link rel="stylesheet" href="https://fonts.googleapis.com/css2?family=Russo+One&display=swap">
<style>
  :root {
    --canvas-bg: #ffffff;
    --leaf-light: #e4f5a0;
    --leaf-mid: #a8d934;
    --leaf-deep: #5f9e1a;
    --word-top: #6f8f2c;
    --word-mid: #3a5a16;
    --word-bottom: #1f340a;
    --word-shadow: rgba(20, 30, 10, 0.55);
  }
  * { margin: 0; padding: 0; box-sizing: border-box; }
  html, body {
    width: 1200px;
    height: 226px;
    overflow: hidden;
    background: var(--canvas-bg);
  }
  .sign {
    position: relative;
    width: 1200px;
    height: 226px;
    background: var(--canvas-bg);
    overflow: hidden;
  }
  .sign__foliage {
    position: absolute;
    inset: 0;
    width: 1200px;
    height: 226px;
  }
  .sign__word {
    position: absolute;
    left: 240px;
    top: 34px;
    width: 710px;
    font-family: "Russo One", sans-serif;
    font-size: 172px;
    line-height: 1;
    letter-spacing: 8px;
    text-align: center;
    background: linear-gradient(180deg, var(--word-top) 0%, var(--word-mid) 45%, var(--word-bottom) 100%);
    -webkit-background-clip: text;
    background-clip: text;
    color: transparent;
    filter: drop-shadow(6px 8px 5px var(--word-shadow));
  }
</style>
</head>
<body>
  <main class="sign">
    <svg class="sign__foliage" viewBox="0 0 1200 226" role="img" aria-label="Fresh green leaf sprays sweeping diagonally from lower left to upper right">
      <defs>
        <linearGradient id="foliage-tone" x1="0" y1="1" x2="1" y2="0">
          <stop offset="0" stop-color="var(--leaf-deep)"/>
          <stop offset="0.45" stop-color="var(--leaf-mid)"/>
          <stop offset="0.8" stop-color="var(--leaf-light)"/>
          <stop offset="1" stop-color="var(--leaf-mid)"/>
        </linearGradient>
        <filter id="foliage-soften" x="-10%" y="-30%" width="120%" height="160%">
          <feGaussianBlur stdDeviation="10"/>
        </filter>
      </defs>
      <path d="M0 226 L0 170 C 220 150, 420 150, 620 105 C 820 60, 960 20, 1060 0 L1200 0 L1200 70 C 1040 90, 900 140, 720 175 C 520 215, 300 220, 0 226 Z"
            fill="url(#foliage-tone)" filter="url(#foliage-soften)" opacity="0.9"/>
    </svg>
    <h1 class="sign__word">MOTEL</h1>
  </main>
</body>
</html>
```